New Architectural Firm Business Cards

New Business card to compliment previous pixel forum logo (attached). Please design a business card that is simple, modern, creative....please do not use "symbols", simply the logo and associated graphics/text. The front should contain name/address/phone/email/web address (with graphics).....back should be 100% graphic design using the logo somehow. Hoping for a two color (black and yellow) design. full bleed design, no borders

Target Market(s)

Commercial Architecture Clients

Industry/Entity Type

Architecture

Contact Information for Business Card

Please design a business card that is simple, modern, creative....please do not use "symbols", simply the logo and associated graphics/text. The front should contain name/address/phone/email/web address (with graphics).....back should be 100% graphic design using the logo somehow

Font styles to use
Sans Serif

Colors
FFF300
FFF600
FEFA6F
FFFEC7
FFFEE8

Requirements
Must have
• Clean, Modern Design
Should not have
• Stock images or "icons"

```html
<!DOCTYPE html>
<html lang="en">
<head>
<meta charset="utf-8">
<title>Norvale Architecture – Business Cards</title>
<link rel="stylesheet" href="https://fonts.googleapis.com/css2?family=Heebo:wght@400;500;700&display=swap">
<style>
  :root {
    --backdrop: #e4e4e4;
    --card-dark: #231f20;
    --card-dark-hi: #3a3637;
    --brand-yellow: #f7bd1a;
    --brand-yellow-hi: #fbd02a;
    --text-light: #ffffff;
  }
  * { margin: 0; padding: 0; box-sizing: border-box; }
  html, body {
    width: 1200px; height: 1200px; overflow: hidden;
    background: var(--backdrop);
    font-family: "Heebo", Arial, sans-serif;
  }
  .canvas { position: relative; width: 1200px; height: 1200px; }
  .card {
    position: absolute; left: 262px; width: 686px; height: 392px;
    border-radius: 26px; overflow: hidden;
    background: linear-gradient(135deg, var(--card-dark) 40%, var(--card-dark-hi) 100%);
    box-shadow: 0 14px 24px rgba(0,0,0,.22);
  }
  .card--front { top: 165px; }
  .card--back { top: 653px; }

  .front-panel {
    position: absolute; left: 0; top: 0; bottom: 0; width: 300px;
    background: linear-gradient(160deg, var(--brand-yellow-hi), var(--brand-yellow));
    display: flex; align-items: center; justify-content: center;
  }
  .front-panel .brand-name {
    font-size: 40px; font-weight: 700; color: var(--card-dark); letter-spacing: 1px;
  }
  .contact {
    position: absolute; right: 57px; top: 150px; text-align: right;
    color: var(--text-light); font-size: 16.5px; line-height: 20px;
  }
  .contact .person-name {
    color: var(--brand-yellow); font-size: 23px; font-weight: 700; line-height: 26px; letter-spacing: .3px;
  }
  .contact .person-role { margin-bottom: 10px; }
  .contact .address { margin-bottom: 10px; }
  .contact-line { display: flex; justify-content: flex-end; align-items: center; gap: 8px; }
  .contact-line svg { width: 13px; height: 13px; flex: none; }

  .back-mark {
    position: absolute; inset: 0;
    display: flex; flex-direction: column; align-items: center; justify-content: center;
  }
  .back-mark .brand-name {
    color: var(--brand-yellow); font-weight: 700; font-size: 64px; line-height: 1; letter-spacing: 1px;
  }
  .back-mark .brand-sub {
    color: var(--brand-yellow); font-weight: 700; font-size: 30px; letter-spacing: 2px; margin-top: 8px;
  }
</style>
</head>
<body>
<main class="canvas">
  <section class="card card--front">
    <div class="front-panel"><span class="brand-name">Norvale</span></div>
    <div class="contact">
      <div class="person-name">DANIEL REYES</div>
      <div class="person-role">President</div>
      <div class="address">
        Norvale Architecture Group<br>
        1420 Cedar Ridge Road<br>
        Juneau, Alaska 99801
      </div>
      <div class="contact-line">555-014-2738
        <svg viewBox="0 0 16 16" aria-hidden="true"><path fill="var(--brand-yellow)" d="M3.5 1l2.5 3-1.5 2c1 2 3 4 5 5l2-1.5 3 2.5-1.5 2.5C7 15 1 9 1 2.5z"/></svg>
      </div>
      <div class="contact-line">info@norvalearch.com
        <svg viewBox="0 0 16 16" aria-hidden="true"><rect x="1" y="3" width="14" height="10" fill="var(--brand-yellow)"/><path d="M1 3l7 6 7-6" fill="none" stroke="var(--card-dark)" stroke-width="1.3"/></svg>
      </div>
      <div class="contact-line">norvalearch.com
        <svg viewBox="0 0 16 16" aria-hidden="true"><circle cx="8" cy="8" r="7" fill="var(--brand-yellow)"/><path d="M1 8h14M8 1c-3 3.5-3 10.5 0 14M8 1c3 3.5 3 10.5 0 14" fill="none" stroke="var(--card-dark)" stroke-width="1"/></svg>
      </div>
    </div>
  </section>

  <section class="card card--back">
    <div class="back-mark">
      <span class="brand-name">Norvale</span>
      <span class="brand-sub">ARCHITECTURE</span>
    </div>
  </section>
</main>
</body>
</html>
```